Ned Halvorsen Executive Coach Business Card Design

I need a new card design for my Executive Coaching practice. I am a Clinical Psychotherapist and Executive Coach. I help my clients get the most out of life by developing their personal and professional skills and abilities.

I work with senior executives. My design needs to be high end. I am thinking gloss on the front. I am also thinking contemporary. I am going to use a black, grey and red colour scheme on the the website. I am thinking grey with black and red accents. I would also like a water mark included on the card.

Target Market(s)

Senior Executives In major Companies

Industry/Entity Type

Business

Contact Information for Business Card

On the front

Ned Halvorsen
Clinical Psychotherapist and Executive Coach
For Personal and Professional Success

On the Back

Tarwin office
87 Tarwin Vale Road Tarwin

North Sydney Office
Suite 309 / 41 Lathom Street North Sydney

Pellington Street Office
Suite 512 / 218 Pellington Street Sydney CBD

Phone 02 95817364
Email ned@nedhalvorsen.com.au

Requirements
Must have
• Friendly but professional
Water Mark
Gloss Front

```html
<!DOCTYPE html>
<html lang="en">
<head>
<meta charset="utf-8">
<title>Ned Halvorsen – Business Card</title>
<link rel="stylesheet" href="https://fonts.googleapis.com/css2?family=Cinzel:wght@400;600&family=Arimo:wght@400;700&display=swap">
<style>
  :root {
    --backdrop: #e2e2e2;
    --card-white: #ffffff;
    --card-grey: #d9d9d9;
    --ink: #111111;
    --black: #0c0c0c;
    --red: #d9141a;
    --silver: #c9c9c9;
    --paper-text: #ffffff;
  }
  * { margin: 0; padding: 0; box-sizing: border-box; }
  html, body { width: 1200px; height: 900px; overflow: hidden; background: var(--backdrop); }
  .stage { position: relative; width: 1200px; height: 900px; }

  .card {
    position: absolute; left: 100px; top: 164px;
    width: 1000px; height: 572px;
    background: linear-gradient(160deg, var(--card-white) 35%, var(--card-grey) 100%);
    box-shadow: 0 18px 40px rgba(0,0,0,.22);
    overflow: hidden;
    font-family: "Arimo", Arial, sans-serif;
    color: var(--ink);
  }
  .card__art { position: absolute; inset: 0; width: 100%; height: 100%; }

  .name-band {
    position: absolute; top: 0; right: 0;
    width: 680px; height: 160px;
    background: var(--black);
    border: 7px solid var(--red);
    border-top: none; border-right: none;
    color: var(--paper-text);
    padding: 20px 28px 0 34px;
    white-space: nowrap;
  }
  .name-band__name {
    font-family: "Cinzel", Georgia, serif;
    font-weight: 400; font-size: 46px; letter-spacing: 2px; line-height: 1;
  }
  .name-band__role { font-size: 21px; line-height: 1.2; margin-top: 10px; }
  .name-band__tagline { font-size: 21px; line-height: 1.2; }

  .address {
    position: absolute; left: 172px; top: 196px;
    white-space: nowrap;
  }
  .address__label { font-size: 28px; font-weight: 400; line-height: 1.1; margin-bottom: 8px; }
  .address__lines { font-size: 17px; line-height: 1.35; }

  .contact {
    position: absolute; right: 46px; top: 290px;
    font-size: 19px; font-weight: 700; line-height: 1.4;
    white-space: nowrap;
  }
</style>
</head>
<body>
<main class="stage">
  <article class="card" aria-label="Business card for Ned Halvorsen">
    <svg class="card__art" viewBox="0 0 1000 572" preserveAspectRatio="none" aria-hidden="true">
      <rect x="0" y="180" width="26" height="392" fill="var(--black)"/>
      <rect x="36" y="200" width="18" height="372" fill="var(--black)"/>
      <rect x="64" y="220" width="16" height="352" fill="var(--black)"/>
      <rect x="90" y="240" width="18" height="332" fill="var(--black)"/>
      <rect x="118" y="170" width="34" height="402" fill="var(--red)"/>
      <polygon points="330,572 1000,390 1000,432 440,572" fill="var(--red)"/>
      <polygon points="440,572 1000,432 1000,572" fill="var(--black)"/>
      <polygon points="540,572 1000,470 1000,494 650,572" fill="var(--silver)"/>
      <polygon points="710,572 1000,515 1000,532 790,572" fill="var(--silver)"/>
      <polygon points="152,572 330,572 152,440" fill="var(--silver)"/>
    </svg>

    <header class="name-band">
      <h1 class="name-band__name">Ned Halvorsen</h1>
      <p class="name-band__role">Clinical Psychotherapist</p>
      <p class="name-band__tagline">Executive Coach For Personal and Professional Success</p>
    </header>

    <section class="address">
      <h2 class="address__label">Address</h2>
      <p class="address__lines">Tarwin office 87 Tarwin Vale Road Tarwin North Sydney Office Suite 309<br>/ 41 Lathom Street North Sydney Pellington Street Office Suite 512</p>
    </section>

    <section class="contact">
      <p class="contact__phone">Phone 02 95817364</p>
      <p class="contact__email">Email ned@nedhalvorsen.com.au</p>
    </section>
  </article>
</main>
</body>
</html>
```